Brightpine Heating and Cooling inc

Free System Replacement estimate
Financing available
Indoor Air Quality
high efficiency system
Zorvik, Pictaloom, Kindrafold
website info
Se Habla Espanol
Free second opinion
We service all major brand

Target Market(s)

Hvac Home Services

Industry/Entity Type

Hvac

Font styles to use
Sans Serif
Other font styles liked:
• Vorneq letter

Colors
3377b5
9bcb3c

```html
<!DOCTYPE html>
<html lang="en">
<head>
<meta charset="utf-8">
<title>Brightpine Heating and Cooling – Postcard</title>
<link href="https://fonts.googleapis.com/css2?family=Open+Sans:wght@400;600;700;800&family=Oswald:wght@500&display=swap" rel="stylesheet">
<style>
:root{
  --blue:#2c5b86;
  --blue-bright:#3377b5;
  --green:#7dc243;
  --green-soft:#9bcb3c;
  --ink:#1f3f66;
  --paper:#ffffff;
  --stage:#e6e6e6;
  --rule:#b9b9b9;
}
*{box-sizing:border-box;margin:0;padding:0}
html,body{width:1036px;height:1200px;overflow:hidden;background:var(--stage);font-family:"Open Sans",sans-serif}
.card{position:absolute;left:123px;width:790px;height:488px;background:var(--paper);overflow:hidden}
.card--front{top:78px}
.card--back{top:610px}
.card-art{position:absolute;inset:0}
.abs{position:absolute}
.brand{display:flex;align-items:center;gap:10px}
.brand-dot{width:46px;height:46px;border-radius:50%;background:var(--green);flex:none}
.brand-name{font-weight:800;color:var(--blue);line-height:1.05;font-size:26px}
.brand--small .brand-dot{width:30px;height:30px}
.brand--small .brand-name{font-size:17px}
.kicker{font-weight:600;color:var(--green-soft);font-size:16px;letter-spacing:.2px}
.headline{font-weight:700;color:#fff;font-size:26px;line-height:1.15;letter-spacing:.3px}
.perks{list-style:none}
.perks li{display:flex;align-items:center;gap:14px;height:37px;color:var(--green);font-weight:700;font-size:15px;line-height:1.1;text-transform:uppercase}
.icon-box{width:32px;height:32px;border:1.5px solid var(--ink);border-radius:3px;display:flex;align-items:center;justify-content:center;flex:none;background:#fff}
.icon-box span{width:16px;height:16px;background:var(--green);border-radius:2px}
.phone{font-family:"Oswald",sans-serif;font-weight:500;color:#fff;font-size:43px;letter-spacing:1px;display:flex;align-items:center;gap:12px}
.contact{display:flex;gap:26px;color:#fff;font-weight:700;font-size:15px}
.contact span{display:flex;align-items:center;gap:8px}
.emergency{color:#fff;font-weight:800;text-align:center;line-height:.95}
.emergency b{display:block;font-size:50px;letter-spacing:-2px}
.emergency i{font-style:normal;display:block;font-size:22px}
.services-title{font-weight:800;color:var(--blue);font-size:19px;letter-spacing:.3px}
.services{list-style:none}
.services li{display:flex;gap:12px;margin-bottom:8px}
.services h3{color:var(--green);font-size:11.5px;font-weight:700;text-transform:uppercase;line-height:1.1}
.services p{color:var(--ink);font-size:10.5px;line-height:1.25}
.stamp{border:1.5px solid var(--rule)}
.address-line{height:1.5px;background:var(--rule)}
.socials{display:flex;gap:14px;color:var(--ink);font-size:11px;font-weight:600}
.socials span{display:flex;align-items:center;gap:4px}
.socials span::before{content:"";width:10px;height:10px;border:1.5px solid var(--ink);border-radius:50%}
</style>
</head>
<body>

<section class="card card--front">
  <svg class="card-art" viewBox="0 0 790 488" width="790" height="488">
    <defs>
      <linearGradient id="unitScene" x1="0" y1="0" x2="0" y2="1">
        <stop offset="0" stop-color="#dfe2e0"/>
        <stop offset=".55" stop-color="#8e968f"/>
        <stop offset="1" stop-color="#5f7d3e"/>
      </linearGradient>
    </defs>
    <path role="img" aria-label="Outdoor air conditioning unit and air handler beside a house with garden plants" d="M415 0 H790 V440 H425 C470 300 472 130 415 0 Z" fill="url(#unitScene)"/>
    <path d="M415 0 C472 130 470 300 425 440" fill="none" stroke="var(--green)" stroke-width="6"/>
    <polygon points="0,128 455,128 443,228 0,228" fill="var(--blue)"/>
    <circle cx="712" cy="372" r="52" fill="none" stroke="var(--blue)" stroke-width="6"/>
    <polygon points="330,432 790,432 790,488 346,488" fill="var(--blue)"/>
    <path d="M0 418 H292 Q316 418 324 432 L346 488 H0 Z" fill="var(--green)"/>
  </svg>

  <div class="abs brand" style="left:38px;top:30px">
    <div class="brand-dot"></div>
    <div class="brand-name">Brightpine<br><span style="font-size:16px">Heating &amp; Cooling inc</span></div>
  </div>

  <div class="abs" style="left:22px;top:145px">
    <div class="kicker">QUALITY THAT IS GUARANTED</div>
    <div class="headline">Heating and Air Conditioning<br>Comfort Specialist</div>
  </div>

  <ul class="abs perks" style="left:25px;top:242px">
    <li><div class="icon-box"><span></span></div>Free system replacement estimate</li>
    <li><div class="icon-box"><span></span></div>Financing available</li>
    <li><div class="icon-box"><span></span></div>Indoor air quality</li>
    <li><div class="icon-box"><span></span></div>Velmora Technologies high efficiency<br>on the background</li>
  </ul>

  <div class="abs emergency" style="left:650px;top:330px"><b>24/7</b><i>Emergency<br>Services</i></div>

  <div class="abs phone" style="left:26px;top:424px">
    <svg width="30" height="42" viewBox="0 0 30 42"><rect x="3" y="2" width="24" height="38" rx="4" fill="none" stroke="#fff" stroke-width="3"/><rect x="11" y="33" width="8" height="3" fill="#fff"/></svg>
    407-555-0142
  </div>
  <div class="abs contact" style="left:370px;top:448px">
    <span>✉ mara@brightpine365.com</span><span>◍ www.brightpine365.com</span>
  </div>
</section>

<section class="card card--back">
  <svg class="card-art" viewBox="0 0 790 488" width="790" height="488">
    <defs>
      <linearGradient id="toolScene" x1="0" y1="0" x2="1" y2="0">
        <stop offset="0" stop-color="#8a6a4e"/>
        <stop offset=".5" stop-color="#a9b3b6"/>
        <stop offset="1" stop-color="#7f9a66"/>
      </linearGradient>
    </defs>
    <path role="img" aria-label="Technician tool belt with refrigerant manifold gauges" d="M0 0 H420 C440 60 455 130 458 195 H0 Z" fill="url(#toolScene)"/>
    <path d="M420 0 C470 130 470 300 425 450" fill="none" stroke="var(--green)" stroke-width="6"/>
    <polygon points="0,190 470,190 455,240 0,240" fill="var(--blue)"/>
    <circle cx="80" cy="180" r="30" fill="none" stroke="var(--blue)" stroke-width="5"/>
    <polygon points="330,432 790,432 790,488 346,488" fill="var(--blue)"/>
    <path d="M0 418 H292 Q316 418 324 432 L346 488 H0 Z" fill="var(--green)"/>
  </svg>

  <div class="abs emergency" style="left:28px;top:158px"><b style="font-size:40px">24/7</b><i style="font-size:16px">Emergency<br>Services</i></div>
  <div class="abs" style="left:142px;top:198px">
    <div class="kicker" style="font-size:19px">QUALITY THAT IS GUARANTED</div>
    <div style="color:#fff;font-size:12px;font-weight:600;letter-spacing:.5px">LIC# CAC4417290</div>
  </div>

  <div class="abs services-title" style="left:28px;top:250px">OUR SERVICES</div>
  <ul class="abs services" style="left:25px;top:280px;width:420px">
    <li><div class="icon-box"><span></span></div><div><h3>Annual inspections</h3><p>allows a technician to identify dirty coils and burned out contactors before they cause long term damage to your system.</p></div></li>
    <li><div class="icon-box"><span></span></div><div><h3>A/C installation</h3><p>high quality installation of residential and commercial air conditioning with the use of professional equipment .</p></div></li>
    <li><div class="icon-box"><span></span></div><div><h3>Service and repair</h3><p>full range of service and repair options of air conditioning systems, ventilation systems, light commercial and residential split systems.</p></div></li>
  </ul>

  <div class="abs brand brand--small" style="left:480px;top:34px">
    <div class="brand-dot"></div>
    <div class="brand-name">Brightpine<br><span style="font-size:11px">Heating &amp; Cooling inc</span></div>
  </div>
  <div class="abs stamp" style="left:667px;top:22px;width:98px;height:88px"></div>
  <div class="abs address-line" style="left:472px;top:187px;width:298px"></div>
  <div class="abs address-line" style="left:472px;top:240px;width:298px"></div>
  <div class="abs address-line" style="left:472px;top:293px;width:298px"></div>

  <div class="abs socials" style="right:24px;top:396px">
    <span>Kindrafold</span><span>Zorvik</span><span>Pictaloom</span>
  </div>

  <div class="abs phone" style="left:26px;top:424px">
    <svg width="30" height="42" viewBox="0 0 30 42"><rect x="3" y="2" width="24" height="38" rx="4" fill="none" stroke="#fff" stroke-width="3"/><rect x="11" y="33" width="8" height="3" fill="#fff"/></svg>
    407-555-0142
  </div>
  <div class="abs contact" style="left:370px;top:448px">
    <span>✉ mara@brightpine365.com</span><span>◍ www.brightpine365.com</span>
  </div>
</section>

</body>
</html>
```